Redesign of Brochure of company services

We need a redesign a brochure. All of the content on the existing brochure correct, but the design we are not pleased with it. I will provide the previous brochure. Every Window Bright is Angolan company that provides multiple service ranging providing fruits, vegetables, fisheries, and meat to multiple industries in angola. Every Window Bright seeks to start delivering or providing their service to home owners looking for fresh products. We want a brochure design that covers all of these aspects.

Target Market(s)

Home owners, middle and upper age mothers, middle and upper class

Industry/Entity Type

Retail

Requirements
Must have
• Logo of the company and the content info
Nice to have
• It's up to you

```html
<!DOCTYPE html>
<html lang="pt">
<head>
<meta charset="utf-8">
<title>Every Window Bright — Frescos ao domicílio</title>
<link rel="stylesheet" href="https://fonts.googleapis.com/css2?family=Didact+Gothic&family=Nunito+Sans:wght@700;800&display=swap">
<style>
  :root {
    --page-bg: #f1eedb;
    --sheet: #ffffff;
    --green: #5fa548;
    --green-dark: #4b8a3b;
    --orange: #f28a2b;
    --red: #e84c28;
    --ink: #1c1c1c;
  }
  * { box-sizing: border-box; margin: 0; padding: 0; }
  html, body { width: 1200px; height: 900px; overflow: hidden; }
  body { background: var(--page-bg); font-family: "Didact Gothic", "Century Gothic", sans-serif; color: var(--ink); position: relative; }
  .brochure { position: absolute; left: 226px; top: 14px; width: 749px; height: 858px; background: var(--sheet); overflow: hidden; }
  .abs { position: absolute; }

  .masthead { left: 0; top: 0; width: 749px; height: 165px; background: var(--green); }
  .masthead__band { left: 0; top: 131px; width: 749px; height: 34px; background: var(--green-dark); }
  .masthead__title { left: 0; top: 30px; width: 749px; text-align: center; color: #fff; font-size: 20.5px; letter-spacing: .2px; }
  .category { top: 59px; width: 132px; }
  .category__photo { width: 132px; height: 78px; }
  .category__label { margin-top: 5px; text-align: center; color: #fff; font-family: "Nunito Sans", sans-serif; font-weight: 700; font-size: 12px; }

  .copy { left: 35px; width: 297px; }
  .copy h2 { font-weight: 400; font-size: 18px; margin-bottom: 5px; }
  .copy p { font-size: 13px; line-height: 14.2px; text-align: justify; margin-bottom: 15px; }
  .trust { left: 414px; top: 190px; width: 300px; }
  .trust h2 { font-weight: 400; font-size: 18px; margin-bottom: 5px; }
  .trust p { font-size: 13px; line-height: 14.2px; }

  .step { left: 391px; width: 345px; height: 45px; display: flex; align-items: center; }
  .step svg { position: absolute; left: 24px; top: 10px; }
  .step span { margin-left: 74px; color: #fff; font-family: "Nunito Sans", sans-serif; font-weight: 700; font-size: 17px; letter-spacing: .4px; }
  .step--order { top: 286px; background: var(--green); }
  .step--pay { top: 337px; background: var(--orange); }
  .step--receive { top: 389px; background: var(--red); }

  .gallery { top: 453px; width: 111px; height: 109px; }

  .promo-photo { left: 13px; top: 569px; width: 352px; height: 199px; background: linear-gradient(135deg, #b98a5a, #8e6a45 60%, #a57b50); }
  .promo-badge { left: 60px; top: 534px; width: 251px; height: 98px; border-radius: 50%; background: var(--orange); border: 4px solid #fff; display: flex; align-items: center; justify-content: center; text-align: center; color: #fff; font-family: "Nunito Sans", sans-serif; font-weight: 800; font-size: 12.5px; line-height: 15px; }

  .origin-photo { left: 391px; top: 569px; width: 345px; height: 199px; background: linear-gradient(160deg, #55613a, #3a4426 55%, #2a301c); }
  .origin-head { left: 391px; top: 569px; width: 345px; height: 32px; background: rgba(35,45,22,.85); color: #fff; font-family: "Nunito Sans", sans-serif; font-weight: 700; font-size: 13px; padding: 10px 0 0 16px; }
  .origin-foot { left: 391px; top: 706px; width: 345px; height: 62px; background: rgba(40,45,28,.75); }
  .origin-brand { left: 403px; top: 728px; width: 90px; color: #fff; font-size: 12px; line-height: 14px; }
  .origin-note { left: 560px; top: 718px; width: 160px; text-align: right; color: #e8e8e8; font-size: 11px; line-height: 13px; }

  .call { top: 768px; height: 76px; background: var(--red); color: #fff; text-align: center; padding-top: 10px; }
  .call strong { display: block; font-family: "Nunito Sans", sans-serif; font-weight: 800; font-size: 18px; }
  .call .phone { display: block; color: #111; font-size: 28px; line-height: 32px; }
  .call--left { left: 13px; width: 352px; }
  .call--right { left: 391px; width: 345px; }
</style>
</head>
<body>
<main class="brochure">
  <header class="abs masthead"></header>
  <div class="abs masthead__band"></div>
  <p class="abs masthead__title">Trazemos frescos da melhor qualidade a bom preço direitinho à sua porta.</p>

  <figure class="abs category" style="left:26px"><div class="category__photo" role="img" aria-label="Hortaliças variadas" style="background:linear-gradient(135deg,#e04a2a,#f3a13b 45%,#4f9a35)"></div><figcaption class="category__label">Hortaliças</figcaption></figure>
  <figure class="abs category" style="left:167px"><div class="category__photo" role="img" aria-label="Frutas tropicais cortadas" style="background:linear-gradient(135deg,#f5b13a,#f1e2c8 50%,#e67a2a)"></div><figcaption class="category__label">Frutas</figcaption></figure>
  <figure class="abs category" style="left:309px"><div class="category__photo" role="img" aria-label="Cortes de carne fresca" style="background:linear-gradient(135deg,#a83a3a,#d78a7e 55%,#8f2f2f)"></div><figcaption class="category__label">Carnes</figcaption></figure>
  <figure class="abs category" style="left:450px"><div class="category__photo" role="img" aria-label="Peixes frescos e salmão" style="background:linear-gradient(135deg,#f08a5a,#c9d0d6 50%,#8d9aa4)"></div><figcaption class="category__label">Peixes</figcaption></figure>
  <figure class="abs category" style="left:591px"><div class="category__photo" role="img" aria-label="Mariscos, caranguejos e camarões" style="background:linear-gradient(135deg,#d9652e,#f0a060 50%,#c4471f)"></div><figcaption class="category__label">Mariscos</figcaption></figure>

  <section class="abs copy" style="top:190px">
    <h2>Hortaliças e Frutas</h2>
    <p>Fornecemos as mais variadas hortaliças, incluindo batata rena, batata doce, alface, abóbora, couve lombarda, couve repolho, couve repolho roxa, cebola, beterraba, beringela, courgette, nabo, feijão verde e milho.</p>
    <h2>Carnes</h2>
    <p>Distribuimos carne fresca de gado ovino, caprino, bovino e suíno e apostamos em produtos de elevada qualidade que nos permitam manter padrões constantes de qualidade dos produtos e dos serviços por nós prestados.</p>
    <h2>Peixes e Mariscos</h2>
    <p>Dispomos de uma vasta gama de peixes e mariscos incluindo pescada, salmão, bacalhau, atum, sardinha, carapau, linguado, camarão, lagostim, gambas, entre outros. Fornecemos o peixe e marisco sempre frescos.</p>
  </section>

  <section class="abs trust">
    <h2>Confie em Qualidade</h2>
    <p>A qualidade de todos os frescos distribuídos por nós é verificada para que apenas os produtos aprovados chegem até si.</p>
  </section>

  <div class="abs step step--order"><svg width="26" height="34" viewBox="0 0 26 34"><path d="M0 0H12L22 10V34H12V14L0 14Z" fill="#3f7f2f"/></svg><span>Encomende por telefone</span></div>
  <div class="abs step step--pay"><svg width="26" height="34" viewBox="0 0 26 34"><path d="M0 0H12L22 10V34H12V14L0 14Z" fill="#d96f16"/></svg><span>Pague no banco</span></div>
  <div class="abs step step--receive"><svg width="26" height="34" viewBox="0 0 26 34"><path d="M0 0H12L22 10V34H12V14L0 14Z" fill="#f59a80"/></svg><span>Receba os seus frescos</span></div>

  <div class="abs gallery" style="left:391px;background:linear-gradient(135deg,#3a2a5a,#e8b23a 45%,#5c9a30)" role="img" aria-label="Frutas variadas com ananás"></div>
  <div class="abs gallery" style="left:508px;background:linear-gradient(135deg,#6b3a22,#b06a3a 50%,#4a2a1a)" role="img" aria-label="Peixe e marisco no mercado"></div>
  <div class="abs gallery" style="left:625px;background:linear-gradient(135deg,#c8442a,#e88a5a 50%,#b83a22)" role="img" aria-label="Camarões e lagostins frescos"></div>

  <div class="abs promo-photo" role="img" aria-label="Legumes frescos sobre mesa de madeira"></div>
  <div class="abs promo-badge">FAZEMOS DESCONTOS A<br>CLIENTES COM CONTRATOS DE<br>FORNECIMENTO CONTÍNUO.</div>
  <div class="abs call call--left"><strong>Manuseamos com cuidado</strong><span class="phone">+244 900 000 123</span></div>

  <div class="abs origin-photo" role="img" aria-label="Agricultor a carregar um cesto num campo verde"></div>
  <div class="abs origin-head">Produtos Nacionais</div>
  <div class="abs origin-foot"></div>
  <div class="abs origin-brand">Every Window Bright</div>
  <p class="abs origin-note">Vendemos apenas produtos nacionais de qualidade controlada</p>
  <div class="abs call call--right"><strong>Não viu o que procura? Ligue já</strong><span class="phone">+244 900 000 123</span></div>
</main>
</body>
</html>
```